Create Product Deck for Organic Beard Oil Brand

We need a product deck to showcase our beard oil collection to potential buyers from department stores, barbershops/salons and wholesale buyers. Attached is a perfect example of the style and layout we want for our product deck.The info regarding the brand should include the following:Company BioPerformance Month OverviewGlobal Reach ShowcaseThe info for each product should include the following:Product NameSKU and/or UPCProduct DescriptionCase SizeWholesale PricingRetail PricingIngredients

Target Market(s)

Men with beards in the U.S.

Women who are married or in a relationship with a bearded man.

Ethnicity: African-American/Multicutural/White

Ages: 24 - 45

Middle Class / Fathers / Married / Dating / Single

Industry/Entity Type

Hair And Beauty

Font styles to use
Sans Serif
Other font styles liked:
• ITC Franklin Gothic

Colors
acd036
0692cd
f04a50

Requirements
Must have
• Must be bright, colorful and showcase each of the products highlighting their particular scents.
• List of our products to be shown in product deck:
• Mango Ginger Beard Oil
• Toasted Pecan Beard Oil
• Built To Last Beard Oil
• Copper Falcon Beard Oil
• Midnight Harbor Beard Oil
• Heritage Reserve Beard Oil
• Images for each of these products have been included as well.
Nice to have
• Surprise me by showing off your personal flash and flare. Do not let our color preferences restrict you from this.
Should not have
• No "bro culture" copy.
• No woodsmen/lumberjack styles like other beard brands have.

```html
<!DOCTYPE html>
<html lang="en">
<head>
<meta charset="UTF-8">
<title>Brand Deck – Performance, Global Reach, Month Overview</title>
<link rel="stylesheet" href="https://fonts.googleapis.com/css2?family=Archivo+Narrow:wght@400;700&display=swap">
<style>
  :root {
    --brand-blue: #2196cc;
    --brand-green: #acd036;
    --paper: #ffffff;
    --ink: #111111;
  }
  * { box-sizing: border-box; margin: 0; padding: 0; }
  html, body { width: 1200px; height: 927px; overflow: hidden; background: var(--paper); }
  .deck-page {
    position: relative;
    width: 1200px;
    height: 927px;
    background: var(--paper);
    font-family: "Archivo Narrow", "Arial Narrow", sans-serif;
    color: var(--ink);
  }
  .header-band {
    position: absolute;
    left: 0; top: 0;
    width: 1200px; height: 463px;
    background: linear-gradient(to bottom, var(--brand-blue) 0%, #5fb1a6 45%, var(--brand-green) 100%);
  }
  .section {
    position: absolute;
    top: 0;
    width: 333px;
  }
  .section--performance { left: 50px; }
  .section--reach { left: 434px; }
  .section--overview { left: 817px; }
  .section-title {
    position: absolute;
    left: 0; width: 333px;
    top: 77px;
    text-align: center;
    color: var(--paper);
    font-weight: 700;
    font-size: 23px;
    line-height: 20px;
    text-transform: uppercase;
    letter-spacing: 0.2px;
  }
  .section-card {
    position: absolute;
    left: 0; top: 146px;
    width: 333px;
    background: var(--paper);
    padding: 27px 18px 0 23px;
  }
  .section-card p {
    font-size: 16px;
    line-height: 18.2px;
    text-align: justify;
    hyphens: manual;
    margin-bottom: 18.2px;
  }
  .section-rule {
    position: absolute;
    left: 0; top: 883px;
    width: 333px; height: 10px;
    background: var(--brand-green);
  }
</style>
</head>
<body>
<main class="deck-page">
  <div class="header-band"></div>

  <section class="section section--performance">
    <h2 class="section-title">Performance</h2>
    <div class="section-card">
      <p>Lorem ipsum dolor sit amet, consectetuer adipiscing elit, sed diam nonummy nibh euismod tincidunt ut laoreet dolore magna aliquam erat volutpat.</p>
      <p>Ut wisi enim ad minim veniam, quis nostrud exerci tation ullamcorper suscipit lobortis nisl ut aliquip ex ea commodo consequat. Duis autem vel eum iriure dolor in hendrerit in vulputate velit esse molestie consequat, vel illum dolore eu feugiat nulla facilisis at vero eros et accumsan et iusto odio dignis&shy;sim qui blandit praesent.</p>
      <p>luptatum zzril delenit augue duis dolore te feugait nulla facilisi.</p>
      <p>Lorem ipsum dolor sit amet, cons ectetuer adipiscing elit, sed diam nonummy nibh euismod tincidunt ut laoreet dolore magna aliquam erat volutpat. Ut wisi enim ad minim veniam, quis nostrud exerci tation ullamcor&shy;per suscipit lobortis nisl ut aliquip ex ea commodo consequat.</p>
      <p>Lorem ipsum dolor sit amet, consectetuer adipiscing elit, sed diam nonummy nibh euismod tincidunt ut laoreet dolore magna aliquam erat volutpat. Ut wisi enim ad minim veniam, quis nostrud exerci tation ullamcor&shy;per suscipit lobortis nisl ut aliquip ex ea commodo consequat.</p>
    </div>
    <div class="section-rule"></div>
  </section>

  <section class="section section--reach">
    <h2 class="section-title">Global Reach<br>Showcase</h2>
    <div class="section-card">
      <p>Lorem ipsum dolor sit amet, consectetuer adipiscing elit, sed diam nonummy nibh euismod tincidunt ut laoreet dolore magna aliquam erat volutpat.</p>
      <p>Ut wisi enim ad minim veniam, quis nostrud exerci tation ullamcorper suscipit lobortis nisl ut aliquip ex ea commodo consequat. Duis autem vel eum iriure dolor in hendrerit in vulputate velit esse molestie consequat, vel illum dolore eu feugiat nulla facilisis at vero eros et accumsan et iusto odio dignis&shy;sim qui blandit praesent.</p>
      <p>luptatum zzril delenit augue duis dolore te feugait nulla facilisi.</p>
      <p>Lorem ipsum dolor sit amet, cons ectetuer adipiscing elit, sed diam nonummy nibh euismod tincidunt ut laoreet dolore magna aliquam erat volutpat. Ut wisi enim ad minim veniam, quis nostrud exerci tation ullamcor&shy;per suscipit lobortis nisl ut aliquip ex ea commodo consequat.</p>
      <p>Lorem ipsum dolor sit amet, consectetuer adipiscing elit, sed diam nonummy nibh euismod tincidunt ut laoreet dolore magna aliquam erat volutpat. Ut wisi enim ad minim veniam, quis nostrud exerci tation ullamcor&shy;per suscipit lobortis nisl ut aliquip ex ea commodo consequat.</p>
    </div>
    <div class="section-rule"></div>
  </section>

  <section class="section section--overview">
    <h2 class="section-title">Month Overview</h2>
    <div class="section-card">
      <p>Lorem ipsum dolor sit amet, consectetuer adipiscing elit, sed diam nonummy nibh euismod tincidunt ut laoreet dolore magna aliquam erat volutpat.</p>
      <p>Ut wisi enim ad minim veniam, quis nostrud exerci tation ullamcorper suscipit lobortis nisl ut aliquip ex ea commodo consequat. Duis autem vel eum iriure dolor in hendrerit in vulputate velit esse molestie consequat, vel illum dolore eu feugiat nulla facilisis at vero eros et accumsan et iusto odio dignis&shy;sim qui blandit praesent.</p>
      <p>luptatum zzril delenit augue duis dolore te feugait nulla facilisi.</p>
      <p>Lorem ipsum dolor sit amet, cons ectetuer adipiscing elit, sed diam nonummy nibh euismod tincidunt ut laoreet dolore magna aliquam erat volutpat. Ut wisi enim ad minim veniam, quis nostrud exerci tation ullamcor&shy;per suscipit lobortis nisl ut aliquip ex ea commodo consequat.</p>
      <p>Lorem ipsum dolor sit amet, consectetuer adipiscing elit, sed diam nonummy nibh euismod tincidunt ut laoreet dolore magna aliquam erat volutpat. Ut wisi enim ad minim veniam, quis nostrud exerci tation ullamcor&shy;per suscipit lobortis nisl ut aliquip ex ea commodo consequat.</p>
    </div>
    <div class="section-rule"></div>
  </section>
</main>
</body>
</html>
```